31 VelvetOrbitals, quotes who will inspire entrepreneurs when create new startups

This project is about 26 quotes that I wrote about create startups, my intention is to share and to inspire another founders o think about theses 26 things before or after create your company. It must be clear, beautiful, with a great design and easy to read, but with strong visual impact. It also important to highlight some powerfull word in each slide, giving something for the audience to remember in each quote

Target Market(s)

Entrepreneurs, investors, startup founders, acelerators

Industry/Entity Type

Startup

Font styles to use
Sans Serif

Colors
f37122
f78f20
fece3e
ffc214
fbed22
fbee3d
8dcce8
33a6d7
0692cd

Requirements
Must have
• Great type and font design, impact, lots of colors
Nice to have
• different fonts, clear message, inspirational
Should not have
• photos,

```html
<!DOCTYPE html>
<html lang="en">
<head>
<meta charset="utf-8">
<title>31 VelvetOrbitals – Startup Quotes</title>
<link rel="stylesheet" href="https://fonts.googleapis.com/css2?family=Open+Sans:ital,wght@0,300;0,400;0,700;0,800;1,400&family=Ubuntu:wght@500;700&display=swap">
<style>
  :root {
    --frame: #4b4b4d;
    --orange: #f37122;
    --orange-light: #f78f20;
    --yellow-light: #fece3e;
    --yellow: #ffc214;
    --blue: #0692cd;
    --grey-dark: #58595b;
    --grey-mid: #7a7a7c;
    --ink: #3a3a3a;
    --white: #ffffff;
    --paper-1: #f4f4f4;
    --paper-2: #d9d9d9;
    --pale-stripe: #fde7a1;
  }
  * { margin: 0; padding: 0; box-sizing: border-box; }
  html, body { width: 1200px; height: 698px; overflow: hidden; background: var(--frame); }
  .deck { position: relative; width: 1200px; height: 698px; background: var(--frame); font-family: "Open Sans", sans-serif; }
  .slide { position: absolute; width: 571px; height: 320px; overflow: hidden; }
  .slide--cover { left: 22px; top: 22px; background: radial-gradient(ellipse at 50% 40%, var(--paper-1), var(--paper-2)); }
  .slide--nice { left: 607px; top: 22px; }
  .slide--ideas { left: 22px; top: 355px; }
  .slide--team { left: 607px; top: 355px; }
  .slide--quote { background: radial-gradient(ellipse at 50% 30%, var(--yellow-light), var(--yellow)); }

  .centered { position: absolute; left: 0; width: 100%; text-align: center; white-space: nowrap; }
  .abs { position: absolute; }

  /* cover */
  .cover-curve { position: absolute; left: 0; top: 0; }
  .brand-mark { top: 34px; height: 30px; line-height: 30px; color: var(--white); font-size: 13px; font-weight: 400; letter-spacing: 1px; }
  .brand-mark .dot { display: inline-block; width: 9px; height: 9px; border-radius: 50%; background: var(--white); margin-right: 7px; vertical-align: 1px; }
  .cover-title { top: 152px; height: 46px; line-height: 46px; font-family: "Ubuntu", sans-serif; font-weight: 700; font-size: 38px; color: var(--orange); }
  .cover-rule { left: 58px; width: 453px; height: 3px; background: var(--grey-mid); }
  .cover-sub { top: 212px; height: 22px; line-height: 22px; font-size: 14px; font-weight: 300; color: var(--ink); }
  .author-pill { left: 226px; top: 257px; width: 119px; height: 18px; line-height: 18px; border-radius: 9px; background: var(--blue); color: var(--white); font-size: 10px; text-align: center; }
  .author-role { top: 280px; height: 12px; line-height: 12px; font-size: 7.5px; font-style: italic; color: var(--ink); }

  /* footer */
  .footer { position: absolute; left: 0; bottom: 0; width: 100%; height: 29px; background: linear-gradient(#f6f6f6, #dedede); }
  .footer-num { position: absolute; left: 13px; top: 8px; width: 16px; height: 12px; background: var(--orange); color: var(--white); font-size: 6.5px; line-height: 12px; text-align: center; font-weight: 700; }
  .footer-copy { position: absolute; left: 36px; top: 8px; line-height: 12px; font-size: 6.5px; color: var(--grey-dark); }
  .footer-brand { position: absolute; right: 12px; top: 8px; line-height: 12px; font-size: 6.5px; color: var(--grey-dark); letter-spacing: .5px; }

  /* shared quote type */
  .headline { color: var(--white); font-weight: 800; text-shadow: 0 1px 2px rgba(0,0,0,.25); }

  /* slide 2 */
  .nice-title { top: 113px; height: 42px; line-height: 42px; font-size: 35px; }
  .nice-line { left: 74px; width: 426px; height: 1.5px; background: var(--grey-dark); }
  .nice-sub { top: 173px; height: 18px; line-height: 18px; font-size: 13.5px; color: var(--grey-dark); }
  .dots { position: absolute; top: 179px; display: flex; gap: 3px; }
  .dots i { width: 6px; height: 6px; border-radius: 50%; background: var(--grey-dark); display: block; }

  /* slide 3 */
  .emblem { position: absolute; left: 222px; top: 25px; width: 128px; height: 128px; border-radius: 50%; background: var(--pale-stripe); box-shadow: 0 1px 4px rgba(0,0,0,.15); }
  .emblem-inner { position: absolute; left: 10px; top: 10px; width: 108px; height: 108px; border-radius: 50%; background: var(--white); }
  .emblem-icon { position: absolute; left: 24px; top: 24px; width: 60px; height: 60px; border-radius: 50%; background: linear-gradient(#e4e4e4, #c9c9c9); }
  .ideas-title { top: 165px; height: 46px; line-height: 46px; font-family: "Ubuntu", sans-serif; font-weight: 700; font-size: 37px; }
  .ideas-sub { top: 225px; height: 24px; line-height: 24px; font-family: "Ubuntu", sans-serif; font-weight: 500; font-size: 19px; color: var(--ink); }
  .ideas-bar { position: absolute; top: 227px; height: 18px; background: var(--pale-stripe); opacity: .85; }

  /* slide 4 */
  .team-top { top: 44px; height: 34px; line-height: 34px; font-size: 27px; }
  .team-ribbon { position: absolute; left: 65px; top: 90px; }
  .team-sub { top: 97px; height: 24px; line-height: 24px; font-size: 19px; font-weight: 400; color: var(--white); }
  .people { position: absolute; top: 102px; display: flex; gap: 5px; }
  .people i { display: block; width: 13px; height: 13px; border-radius: 50%; border: 1.5px solid var(--white); }
  .team-mid { top: 141px; height: 34px; line-height: 34px; font-size: 28px; }
  .team-big { top: 180px; height: 78px; line-height: 78px; font-size: 68px; letter-spacing: -1px; }
</style>
</head>
<body>
<main class="deck">

  <section class="slide slide--cover">
    <svg class="cover-curve" width="571" height="320" viewBox="0 0 571 320" aria-hidden="true">
      <defs>
        <linearGradient id="orangeFill" x1="0" y1="0" x2="0" y2="1">
          <stop offset="0" stop-color="#f89a33"/>
          <stop offset="1" stop-color="#f37122"/>
        </linearGradient>
      </defs>
      <path d="M0,0 L571,0 L571,50 Q286,192 0,57 Z" fill="#58595b"/>
      <path d="M0,0 L571,0 Q286,240 0,0 Z" fill="url(#orangeFill)"/>
    </svg>
    <div class="centered brand-mark"><span class="dot"></span>SWELLPOINT.CO</div>
    <h1 class="centered cover-title">31 VelvetOrbitals</h1>
    <div class="abs cover-rule" style="top:202px"></div>
    <svg class="abs" style="left:58px;top:212px" width="30" height="22" viewBox="0 0 30 22" aria-hidden="true"><path d="M0,0 H30 V22 H0 L9,11 Z" fill="#7a7a7c"/></svg>
    <svg class="abs" style="left:481px;top:212px" width="30" height="22" viewBox="0 0 30 22" aria-hidden="true"><path d="M0,0 H30 L21,11 L30,22 H0 Z" fill="#7a7a7c"/></svg>
    <p class="centered cover-sub">Things to know before or after you create your startup</p>
    <div class="abs cover-rule" style="top:241px"></div>
    <div class="author-pill">Lorenzo Quarle</div>
    <p class="centered author-role">Founder&amp; CEO Swellpoint.Co</p>
  </section>

  <section class="slide slide--quote slide--nice">
    <svg class="abs" style="left:73px;top:122px" width="35" height="26" viewBox="0 0 35 26" aria-hidden="true"><path d="M0,0 H35 V26 H0 L11,13 Z" fill="#ffffff"/></svg>
    <h2 class="centered headline nice-title">BE A NICE PERSON</h2>
    <svg class="abs" style="left:464px;top:122px" width="35" height="26" viewBox="0 0 35 26" aria-hidden="true"><path d="M0,0 H35 L24,13 L35,26 H0 Z" fill="#ffffff"/></svg>
    <div class="nice-line" style="position:absolute;top:162px"></div>
    <div class="nice-line" style="position:absolute;top:166px"></div>
    <div class="dots" style="left:74px"><i></i><i></i><i></i></div>
    <p class="centered nice-sub">You are the first feature that your company will show</p>
    <div class="dots" style="left:474px"><i></i><i></i><i></i></div>
    <div class="nice-line" style="position:absolute;top:201px"></div>
    <div class="nice-line" style="position:absolute;top:205px"></div>
    <footer class="footer"><span class="footer-num">2</span><span class="footer-copy">Copyright © 2017 Swellpoint.Co | All Rights Reserved.</span><span class="footer-brand">SWELLPOINT.CO</span></footer>
  </section>

  <section class="slide slide--quote slide--ideas">
    <div class="emblem">
      <div class="emblem-inner">
        <div class="emblem-icon" role="img" aria-label="Line drawing of a brain"></div>
      </div>
    </div>
    <h2 class="centered headline ideas-title">Nobody cares about ideas</h2>
    <div class="ideas-bar" style="left:46px;width:110px"></div>
    <p class="centered ideas-sub">it’s all about execution</p>
    <div class="ideas-bar" style="left:417px;width:110px"></div>
    <footer class="footer"><span class="footer-num">3</span><span class="footer-copy">Copyright © 2017 Swellpoint.Co | All Rights Reserved.</span><span class="footer-brand">SWELLPOINT.CO</span></footer>
  </section>

  <section class="slide slide--quote slide--team">
    <h2 class="centered headline team-top">SEARCH FOR THE RIGHT PEOPLE</h2>
    <svg class="team-ribbon" width="446" height="38" viewBox="0 0 446 38" aria-hidden="true"><path d="M0,0 H446 L432,19 L446,38 H0 L14,19 Z" fill="#7a7a7c"/></svg>
    <div class="people" style="left:93px"><i></i><i></i><i></i></div>
    <p class="centered team-sub">AND BUILD A GREAT TEAM</p>
    <div class="people" style="left:434px"><i></i><i></i><i></i></div>
    <h2 class="centered headline team-mid">WITHOUT THEM YOU ARE</h2>
    <h2 class="centered headline team-big">NOTHING</h2>
    <footer class="footer"><span class="footer-num">4</span><span class="footer-copy">Copyright © 2017 Swellpoint.Co | All Rights Reserved.</span><span class="footer-brand">SWELLPOINT.CO</span></footer>
  </section>

</main>
</body>
</html>
```